Landscape Lighting Product Brochure

You created a flyer for us that was for our Christmas Light training business and we really liked the design.

We want to mimic something with similar colors of the blue and gold. However, it would be for product sales for our landscape lighting product line. We want the products to really be the star of the show on this brochure that will include product photos as well as quick details of each product.

We also want to highlight that these products carry a lifetime warranty and are made of high quality Brass.

These products are going to be marketed to installers so not so much your average home owner.

It should also include our logo and contact information, same as the previous flyer.

Target Market(s)

Installers who are looking to purchase high quality materials

Requirements
Must have
• Must be 1 page with all of our products listed. Must have our logo.
Nice to have
• It would be nice to have a small section of details for each product.

```html
<!DOCTYPE html>
<html lang="en">
<head>
<meta charset="UTF-8">
<title>Beacon Glow – Landscape Lighting Products</title>
<link href="https://fonts.googleapis.com/css2?family=Poppins:wght@400;500;600;700;800&display=swap" rel="stylesheet">
<style>
  :root {
    --ink: #070707;
    --gold: #f2b824;
    --blue: #1570e0;
    --white: #ffffff;
    --text-dark: #1f1a10;
    --rule: #e4e4e4;
    --page-bg: #dcdcdc;
  }
  * { margin: 0; padding: 0; box-sizing: border-box; }
  html, body { width: 816px; height: 1200px; overflow: hidden; background: var(--page-bg); }
  body { font-family: "Poppins", Arial, sans-serif; }

  .flyer { position: relative; width: 816px; height: 1200px; background: var(--white); overflow: hidden; }

  .hero { position: absolute; left: 0; top: 0; width: 816px; height: 580px; background: var(--ink); }
  .brand { position: absolute; top: 76px; left: 0; width: 100%; text-align: center; }
  .brand-name { display: block; color: var(--blue); font-weight: 700; font-size: 40px; letter-spacing: 2px; line-height: 1; }

  .hero-photo {
    position: absolute; left: 0; top: 160px; width: 816px; height: 260px;
    background:
      radial-gradient(ellipse 60% 45% at 40% 55%, rgba(150,95,55,.55), transparent 70%),
      radial-gradient(ellipse 30% 30% at 80% 60%, rgba(130,80,45,.45), transparent 70%),
      linear-gradient(180deg, #070707 0%, #1d1610 35%, #2a1f16 65%, #070707 100%);
  }

  .title { position: absolute; top: 420px; left: 0; width: 100%; text-align: center; line-height: 1; }
  .title-main { display: block; color: var(--white); font-weight: 700; font-size: 86px; letter-spacing: 1px; }
  .title-sub { display: block; margin-top: 4px; font-size: 52px; }
  .title-sub .gold { color: var(--gold); font-weight: 700; }
  .title-sub .blue { color: var(--blue); font-weight: 500; }

  .footer-band { position: absolute; left: 0; top: 1048px; width: 816px; height: 152px; background: var(--blue); border-radius: 14px 14px 0 0; }

  .col-rule { position: absolute; top: 584px; width: 1px; height: 460px; background: var(--rule); }

  .product-grid {
    position: absolute; left: 55px; top: 587px; width: 705px;
    display: grid; grid-template-columns: repeat(4, 173px); column-gap: 5px;
    grid-template-rows: 118px 149px 118px 149px;
  }
  .product-shot {
    align-self: center; justify-self: center; width: 120px; height: 92px; border-radius: 6px;
    background: radial-gradient(circle at 50% 45%, #8d8578 0%, #4a4540 55%, #f4f4f4 100%);
  }
  .product-shot.path { width: 30px; }
  .product-shot.bulb { background: radial-gradient(circle at 50% 50%, #f3e7b7 0%, #d9d4c8 60%, #f5f5f5 100%); }

  .spec-card { background: var(--gold); border-radius: 8px; padding: 12px 12px 10px 13px; color: var(--text-dark); }
  .spec-title { font-weight: 700; font-size: 12px; line-height: 1.1; margin-bottom: 5px; text-transform: uppercase; }
  .spec { margin-bottom: 5px; }
  .spec-label {
    position: relative; display: block; padding-left: 13px;
    color: var(--blue); font-weight: 700; font-size: 10px; line-height: 1.2; text-transform: uppercase;
  }
  .spec-label::before {
    content: ""; position: absolute; left: 0; top: 2px; width: 9px; height: 9px;
    border: 1.5px solid var(--white); border-radius: 1px;
  }
  .spec-label::after {
    content: ""; position: absolute; left: 3px; top: 1px; width: 4px; height: 7px;
    border-right: 2px solid var(--text-dark); border-bottom: 2px solid var(--text-dark); transform: rotate(40deg);
  }
  .spec-value { display: block; padding-left: 13px; font-size: 9.5px; line-height: 1.2; }
  .spec-value.colors { word-spacing: 8px; }

  .contact-bar {
    position: absolute; left: 55px; top: 1140px; width: 705px; height: 34px;
    display: flex; align-items: center; color: var(--white);
  }
  .phone { display: flex; align-items: center; gap: 4px; font-size: 22px; font-weight: 500; }
  .divider { width: 1px; height: 26px; background: rgba(255,255,255,.6); margin: 0 36px 0 34px; }
  .follow { display: flex; align-items: center; gap: 5px; font-size: 11px; font-weight: 500; }
  .social-dot { width: 15px; height: 15px; border-radius: 50%; background: var(--white); }
  .website { margin-left: auto; font-size: 22px; letter-spacing: .5px; }
  .website strong { color: var(--gold); font-weight: 700; }
</style>
</head>
<body>
<main class="flyer">
  <section class="hero">
    <div class="brand">
      <span class="brand-name">BEACON GLOW</span>
    </div>
    <div class="hero-photo" role="img" aria-label="Night photo of a brick house outlined with red and white holiday lights"></div>
    <h1 class="title">
      <span class="title-main">LANDSCAPE</span>
      <span class="title-sub"><span class="gold">LIGHTING</span> <span class="blue">PRODUCTS</span></span>
    </h1>
  </section>

  <div class="footer-band"></div>
  <div class="col-rule" style="left:231px"></div>
  <div class="col-rule" style="left:409px"></div>
  <div class="col-rule" style="left:587px"></div>

  <section class="product-grid">
    <div class="product-shot bulb" role="img" aria-label="Three LED G4 bi-pin bulbs"></div>
    <div class="product-shot" role="img" aria-label="Bronze brass up light fixture on a ground stake"></div>
    <div class="product-shot" role="img" aria-label="Die-cast brass up light fixture with flat lens"></div>
    <div class="product-shot" role="img" aria-label="Two black in-ground light fixtures"></div>

    <article class="spec-card">
      <h2 class="spec-title">LED G4 (Silicone<br>or Ceramic)</h2>
      <p class="spec"><span class="spec-label">Materials</span><span class="spec-value">Silicone or Ceramic</span></p>
      <p class="spec"><span class="spec-label">LED Color Aviable</span><span class="spec-value colors">Red Green Blue Amber</span></p>
      <p class="spec"><span class="spec-label">Warranty</span><span class="spec-value">3 years warranty</span></p>
    </article>
    <article class="spec-card">
      <h2 class="spec-title">Up Light Fixtures</h2>
      <p class="spec"><span class="spec-label">Materials</span><span class="spec-value">Cast brass.</span></p>
      <p class="spec"><span class="spec-label">Lens</span><span class="spec-value">Clear convex glass lens</span></p>
      <p class="spec"><span class="spec-label">Warranty</span><span class="spec-value">Limited lifetime warranty</span></p>
    </article>
    <article class="spec-card">
      <h2 class="spec-title">Up Light Fixtures</h2>
      <p class="spec"><span class="spec-label">Materials</span><span class="spec-value">Die-cast brass</span></p>
      <p class="spec"><span class="spec-label">Lens</span><span class="spec-value">Clear flat glass lens</span></p>
      <p class="spec"><span class="spec-label">Warranty</span><span class="spec-value">Limited lifetime warranty</span></p>
    </article>
    <article class="spec-card">
      <h2 class="spec-title">In Ground<br>Light Fixtures</h2>
      <p class="spec"><span class="spec-label">Materials</span><span class="spec-value">Die-cast brass,PVC</span></p>
      <p class="spec"><span class="spec-label">Lens</span><span class="spec-value">Shock resistant glass lens</span></p>
      <p class="spec"><span class="spec-label">Warranty</span><span class="spec-value">Limited lifetime warranty</span></p>
    </article>

    <div class="product-shot path" role="img" aria-label="Brass path light fixture on a stem"></div>
    <div class="product-shot" role="img" aria-label="LED MR16 lamp with black housing"></div>
    <div class="product-shot" role="img" aria-label="LED PAR36 AR111 lamp"></div>
    <div class="product-shot" role="img" aria-label="Stainless steel lighting transformers"></div>

    <article class="spec-card">
      <h2 class="spec-title">Path Light Fixtures</h2>
      <p class="spec"><span class="spec-label">Materials</span><span class="spec-value">Cast brass.</span></p>
      <p class="spec"><span class="spec-label">Lens</span><span class="spec-value">Shock resistant,frosted<br>glass lens</span></p>
      <p class="spec"><span class="spec-label">Warranty</span><span class="spec-value">Limited lifetime warranty</span></p>
    </article>
    <article class="spec-card">
      <h2 class="spec-title">LED MR 16(6 LED )</h2>
      <p class="spec"><span class="spec-label">Materials</span><span class="spec-value">Die-cast Aluminium</span></p>
      <p class="spec"><span class="spec-label">LED Color Aviable</span><span class="spec-value colors">Red Green Blue Amber</span></p>
      <p class="spec"><span class="spec-label">Warranty</span><span class="spec-value">5 Years warranty</span></p>
    </article>
    <article class="spec-card">
      <h2 class="spec-title">LED PAR36/AR 111</h2>
      <p class="spec"><span class="spec-label">Materials</span><span class="spec-value">Die-cast Aluminium</span></p>
      <p class="spec"><span class="spec-label">LED Color Aviable</span><span class="spec-value colors">Red Green Blue Amber</span></p>
      <p class="spec"><span class="spec-label">Warranty</span><span class="spec-value">5 Years warranty</span></p>
    </article>
    <article class="spec-card">
      <h2 class="spec-title">Transformars</h2>
      <p class="spec"><span class="spec-label">Materials</span><span class="spec-value">304 stainless steel</span></p>
      <p class="spec"><span class="spec-label">Power Cord</span><span class="spec-value">6' in leangth</span></p>
      <p class="spec"><span class="spec-label">Warranty</span><span class="spec-value">Limited lifetime warranty</span></p>
    </article>
  </section>

  <footer class="contact-bar">
    <div class="phone">
      <svg width="18" height="18" viewBox="0 0 24 24" aria-hidden="true"><path d="M6.6 10.8a15.1 15.1 0 0 0 6.6 6.6l2.2-2.2a1 1 0 0 1 1-.25 11.4 11.4 0 0 0 3.6.57 1 1 0 0 1 1 1V20a1 1 0 0 1-1 1A17 17 0 0 1 3 4a1 1 0 0 1 1-1h3.5a1 1 0 0 1 1 1c0 1.250.2 2.45.57 3.57a1 1 0 0 1-.25 1z" fill="none" stroke="#f2b824" stroke-width="2"/></svg>
      <span>555-014-2290</span>
    </div>
    <span class="divider"></span>
    <div class="follow">
      <span>Follow Us</span>
      <span class="social-dot"></span><span class="social-dot"></span><span class="social-dot"></span>
    </div>
    <div class="website">www.<strong>beaconglowpro</strong>.com</div>
  </footer>
</main>
</body>
</html>
```